Super-fantastic-interesting infographic of terribly boring content

-Looking to provide a visually engaging snapshot of the average Canadian investor.
-Help people compare their personal financial situation against the infographic (Average).
-We want viewers to feel engaged and interested in the info presented, not confused and irritated.

Data points to present:

The average Canadian snapshot:
* Average Canadian household Income in 2016: $76,900
* Median Net Worth of Canadian families in 2016: $295,100
* Average annual household expenditures on goods a& services: $62,183
* Median value in principal residence: $349,000
* Highest net annual savings amount (Age 35-44): $10,120
* Number of Canadian families holding a mortgage: 38.4%
* Median Mortgage value of Principal residence: $190,000
* Debt to disposable income ratio average: 172.1
* Total value of all assets held by Canadians in 2016: 12 Trillion dollars
* The principal residence was the single largest asset held (of the 12 Trillion): 32%
* Private pensions was the 2nd largest grouping of assets at 29.2%
* The average borrowing rate for Canadian mortgages: 2.94%
* 74% were fixed rate, 21% were variable and 5% blended.
* 48% of Canadians do not save or invest at all
* 54% of Canadians do not budget regularly
* 1 in 3 Canadians have lost at least 20% in one year
* 51% of Canadians took NO ACTION after losing at least 20% in one year.
* 22% of those people either, hired or fired an advisor

Financial advice landscape:
* # of households in Canada: 13,300,000
* Households with an advisor 5,300,000
* % of households dissatisfied with existing advisor 1,100,000

Target Market(s)

Investors, ages 22-55

Industry/Entity Type

Financial

Font styles to use
Sans Serif

Colors

Designer to choose colors to be used in the design.

Requirements
Must have
• Header: Financial landscape of the average Canadian
Nice to have
• There is a lot of numbers and percentages, find a way to deliver the info using a mix of images, numbers, pictures etc.

```html
<!DOCTYPE html>
<html lang="en">
<head>
<meta charset="utf-8">
<title>Financial Landscape of the Average Canadian 2016-2017</title>
<link href="https://fonts.googleapis.com/css2?family=Roboto+Condensed:wght@300;400;700&family=Roboto:wght@300;400;500;700&display=swap" rel="stylesheet">
<style>
:root{
  --green:#1fa85a;
  --red:#d62a2e;
  --maple:#d9403c;
  --ink:#111;
  --blue:#2a78b8;
  --steel:#54707f;
  --sky:#5596b6;
  --teal:#7ecbc0;
  --periwinkle:#7f90c8;
  --yellow:#fdf08c;
  --gold:#f7bf3a;
  --purple:#7b5aa6;
  --grey:#5a5a5a;
  --pale:#eef2ee;
  --pole:#c9cfd1;
}
*{box-sizing:border-box;margin:0;padding:0}
html,body{width:1200px;height:780px;overflow:hidden;background:#fff}
body{font-family:"Roboto",Arial,sans-serif;color:var(--ink)}
.canvas{position:relative;width:1200px;height:780px}
.abs{position:absolute}
.fill{position:absolute;border-radius:4px}

.title{left:30px;top:22px;font-family:"Roboto Condensed",sans-serif;font-weight:700;color:var(--green);font-size:66px;line-height:58px;letter-spacing:-2px}
.subtitle{right:28px;top:22px;text-align:right;font-family:"Roboto Condensed",sans-serif;font-weight:700;color:var(--red);font-size:37px;line-height:35px;letter-spacing:-1px}
.subtitle .years{color:var(--ink);font-size:40px;line-height:44px;letter-spacing:0}
.rule{left:30px;top:146px;width:1140px;border-top:1.5px dashed #555}

.section-title{left:255px;top:168px;font-family:"Roboto Condensed",sans-serif;font-weight:300;font-size:24px;letter-spacing:-.5px}

.asset-share{font-size:10px;line-height:11px;color:var(--blue)}
.asset-share b{font-size:17px;line-height:18px;font-weight:700;display:block}
.asset-share strong{font-weight:700}

.trillion{left:34px;top:323px;width:181px;height:64px;background:var(--pale);border-radius:8px;text-align:center;color:var(--blue);padding-top:6px}
.trillion b{display:block;font-family:"Roboto Condensed",sans-serif;font-size:26px;line-height:26px}
.trillion span{font-size:12px;line-height:14px;font-weight:300;display:block}

.household-list{left:243px;top:312px;width:252px;height:90px;background:#f6f7f6;padding:5px 0 0 34px;font-size:8px;color:var(--grey)}
.household-list div{margin-bottom:4px;position:relative}
.household-list div::before{content:"";position:absolute;left:-26px;top:2px;width:18px;height:16px;background:#9bb4cc;border-radius:2px}
.household-list b{display:block;font-size:13px;line-height:13px;color:#333}
.household-list .without b,.household-list .without{color:var(--red)}

.sign{color:#fff;border-radius:3px}
.sign-main{left:508px;top:210px;width:182px;height:102px;background:var(--sky);padding:12px 0 0 17px}
.sign-main b{display:block;font-size:29px;line-height:30px;font-weight:500}
.sign-main span{display:block;font-size:21px;line-height:20px;font-weight:500}
.sign-home{left:500px;top:330px;width:100px;height:46px;background:var(--periwinkle);text-align:center;padding-top:3px}
.sign-home b{display:block;font-family:"Roboto Condensed",sans-serif;font-size:21px;line-height:22px}
.sign-home span{font-size:7px;line-height:7px;display:block}
.pole{background:var(--pole)}

.stat-card{left:700px;width:100px;padding:6px 0 0 8px;color:#fff;border-radius:3px}
.stat-card b{display:block;font-family:"Roboto Condensed",sans-serif;font-size:24px;line-height:24px;font-weight:700}
.stat-card span{display:block;font-size:7px;line-height:8px}
.stat-card i{position:absolute;right:0;top:-4px;background:var(--gold);color:var(--ink);font-style:normal;font-size:11px;font-weight:700;padding:1px 5px;border-radius:2px}
.income{top:190px;height:62px;background:var(--teal);padding-top:14px}
.income b{color:#6a6a6a}.income span{color:#6a8f8a}
.spend{top:258px;height:66px;background:var(--red);padding-top:15px}
.worth{top:332px;height:58px;background:var(--green);padding-top:12px}

.mortgage{left:822px;top:180px;width:350px;height:438px;background:var(--yellow);border-radius:0 0 14px 0;padding:24px 0 0 30px}
.mortgage-fold{left:765px;top:506px;width:70px;height:112px;background:var(--gold);border-radius:40px 0 0 40px}
.mortgage .about{font-family:"Roboto Condensed",sans-serif;font-size:18px;color:var(--blue);font-weight:700;line-height:18px}
.mortgage .heading{font-family:"Roboto Condensed",sans-serif;font-size:49px;line-height:48px;color:var(--blue);font-weight:700;letter-spacing:-1px;border-bottom:1px dashed #c5b96a;width:218px;padding-bottom:4px}
.mortgage .badge{position:absolute;left:262px;top:38px;width:66px;height:66px;border-radius:50%;background:var(--gold);border:3px solid #fbd66c}
.mort-stat{font-family:"Roboto Condensed",sans-serif;line-height:44px;font-size:44px;letter-spacing:-1px}
.mort-note{font-size:12.5px;color:var(--grey);margin-bottom:14px}
.mort-note b{font-weight:500}
.rates{border:1px dashed #8a9bc7;width:157px;padding:3px 10px;font-size:15px;line-height:19px;color:var(--grey)}

.habit{left:22px;top:421px;width:728px;height:317px;background:var(--steel)}
.habit-tab{left:616px;top:421px;width:134px;height:76px;background:var(--yellow);text-align:right;padding:6px 14px 0 0;font-family:"Roboto Condensed",sans-serif;font-weight:700;font-size:29px;line-height:30px;color:var(--steel)}
.ring{width:142px;height:142px;border-radius:50%}
.habit-stat{color:#fff;text-align:center;font-weight:300;font-size:14px;line-height:16px}
.habit-stat b{display:block;font-weight:700;font-size:38px;line-height:40px}
.habit-stat strong{font-weight:700}
.ratio{left:640px;top:508px;width:110px}
.ratio b{font-size:30px;line-height:32px}
.ratio span{font-size:12px;line-height:14px;display:block}
.reaction{left:643px;width:90px;text-align:center;color:var(--red)}
.reaction b{display:block;font-family:"Roboto Condensed",sans-serif;font-size:27px;line-height:26px;font-weight:700}
.reaction span{font-size:10px;line-height:11px;display:block}
.did-nothing{top:602px;height:50px;background:var(--red);color:#fff;padding-top:6px}
.did-nothing span{font-weight:700}
.hired{top:656px;height:58px;background:#fff;padding-top:6px}

.brand{left:910px;top:662px;display:flex;align-items:center;gap:10px}
.brand-dot{width:50px;height:50px;border-radius:50%;background:#2d7ec6}
.brand-name{font-family:"Roboto",sans-serif;font-weight:400;font-size:34px;color:#333;letter-spacing:-.5px}
</style>
</head>
<body>
<main class="canvas">

  <h1 class="abs title">FINANCIAL<br>LANDSCAPE</h1>
  <div class="fill" role="img" aria-label="Banknote with stacks of gold coins" style="left:372px;top:62px;width:152px;height:66px;background:linear-gradient(90deg,#f2c94c,#7ea94f 30%,#7ea94f 70%,#f2c94c)"></div>
  <div class="fill" role="img" aria-label="Steel safe" style="left:538px;top:52px;width:68px;height:70px;background:#6d8a98"></div>
  <div class="fill" role="img" aria-label="Small house" style="left:625px;top:50px;width:84px;height:72px;background:linear-gradient(#3e8a3e 0 38%,#9fb6d6 38%)"></div>

  <div class="fill" role="img" aria-label="Red maple leaf" style="left:900px;top:38px;width:90px;height:90px;background:var(--maple);border-radius:40% 40% 10% 10%"></div>
  <div class="abs subtitle">of average<br>Canadian<div class="years">2016-2017</div></div>
  <div class="abs rule"></div>

  <h2 class="abs section-title">FINANCIAL ADVICE LANDSCAPE</h2>

  <div class="abs asset-share" style="left:24px;top:202px;width:60px;text-align:right"><b>29.2%</b>of assets being held by <strong>private pensions</strong></div>
  <div class="fill" role="img" aria-label="Maple leaf split into asset shares" style="left:84px;top:226px;width:92px;height:90px;background:linear-gradient(90deg,#f08c84,var(--maple));border-radius:40% 40% 10% 10%"></div>
  <div class="abs asset-share" style="left:168px;top:200px;width:64px"><b>32%</b>of assets being held by <strong>principal residences</strong></div>

  <div class="abs trillion"><b>$12 TRILLION</b><span>total value of assets<br>Canadian holds in 2016</span></div>

  <div class="fill" role="img" aria-label="Grid of ten houses showing share of households with an advisor" style="left:237px;top:212px;width:260px;height:92px;background:linear-gradient(90deg,#8fa9c9 0 40%,#c6a2a8 40%)"></div>

  <div class="abs household-list">
    <div><b>5,300,000</b>households <strong>with</strong> financial advisor</div>
    <div class="without"><b>8,000,000</b>households <strong>without</strong> financial advisor</div>
    <div><b>1,100,000</b>dissatisfied households <strong>with</strong> current financial advisor</div>
  </div>

  <div class="abs pole" style="left:594px;top:312px;width:10px;height:88px"></div>
  <svg class="abs" style="left:686px;top:215px" width="20" height="140"><path d="M0 40 L14 10 M0 70 L14 70 M0 90 L14 125" stroke="var(--pole)" stroke-width="4"/></svg>
  <div class="abs sign sign-main"><b>13,300,000</b><span>households<br>in Canada</span></div>
  <div class="abs sign sign-home"><b>$349,000</b><span>median value in<br>principal residence</span></div>

  <div class="abs stat-card income"><i>2016</i><b>$76,900</b><span>average annual<br>household income</span></div>
  <div class="abs stat-card spend"><i>2016</i><b>$62,183</b><span>average annual<br>household expenditures<br>(goods &amp; services)</span></div>
  <div class="abs stat-card worth"><i>2016</i><b>$295,100</b><span>median net worth<br>of Canadian families</span></div>

  <div class="abs mortgage-fold"></div>
  <section class="abs mortgage">
    <div class="about">about</div>
    <div class="heading">MORTGAGE</div>
    <div class="badge"></div>
    <div class="mort-stat" style="color:var(--purple);margin-top:6px">38.4%</div>
    <div class="mort-note">number of Canadian families <b>holding a mortgage</b></div>
    <div class="mort-stat" style="color:var(--blue);margin-top:4px">$190,000</div>
    <div class="mort-note">median mortgage value of principal residence.</div>
    <div class="mort-stat" style="color:var(--periwinkle);margin-top:14px">2.94%</div>
    <div class="mort-note" style="margin-bottom:6px">average borrowing rate for Canadian mortgages</div>
    <div class="rates">74% fixed rate<br>21% variable rate<br>5% blended rate</div>
  </section>

  <section class="abs habit"></section>
  <div class="abs habit-tab">FINANCE<br>HABIT</div>

  <div class="abs ring" role="img" aria-label="Safe with a banknote going in" style="left:38px;top:482px;background:radial-gradient(#fff 0 52%,var(--red) 53%)"></div>
  <div class="abs ring" role="img" aria-label="Torn budget sheet" style="left:203px;top:482px;background:radial-gradient(#fde58a 0 48%,var(--red) 49%)"></div>
  <div class="abs ring" role="img" aria-label="Safe for ages 35 to 44" style="left:363px;top:482px;background:#eef0ee"></div>
  <div class="fill" role="img" aria-label="Three figures, one outlined with question marks" style="left:510px;top:490px;width:130px;height:120px;background:linear-gradient(90deg,#c8d0d4 0 38%,var(--red) 38%)"></div>

  <div class="abs habit-stat" style="left:40px;top:632px;width:140px"><b>48%</b>do not save or<br>do not invest<br><strong>at all.</strong></div>
  <div class="abs habit-stat" style="left:204px;top:632px;width:140px"><b>54%</b>do not budget<br>regularly</div>
  <div class="abs habit-stat" style="left:356px;top:626px;width:156px"><b style="font-size:40px;line-height:44px">$10,120</b>highest net<br>annual savings<br>in 2016</div>
  <div class="abs habit-stat" style="left:520px;top:626px;width:126px"><b style="font-size:40px;line-height:44px">1 of 3</b>have lost 20%<br>of their assets<br>in one year</div>
  <div class="abs habit-stat ratio"><b>172:1</b><span>debt to<br>disposable<br>income ratio</span></div>

  <div class="abs reaction did-nothing"><b>51%</b><span>do NOTHING!</span></div>
  <div class="abs reaction hired"><b>22%</b><span>hired/fired<br>financial advisor</span></div>

  <div class="abs brand"><div class="brand-dot"></div><div class="brand-name">NorthLedger</div></div>

</main>
</body>
</html>
```